Building company buisness cards

We are looking for a sharp modern new look for our business cards.We are a New Zealand based company that specialises in house and land packages.We have attached a photo of the current logo and would like to see if it can be improved somehow if needed.We are open to any colours but we have chosen Black and White at this stage. Feel free to change the font and make the logo smarter looking.Play with the colours and see what looks best.We want a card that looks so good know one will want to throw it away!

Target Market(s)

Building profesonals, home buyers

Industry/Entity Type

Building

Contact Information for Business Card

Derek Haskins
0274930268
derekh@stonerange.co.nz

Font styles to use
Serif
Sans Serif

Colors

Designer to choose colors to be used in the design.

Requirements
Must have
• Just the logo on one side and details on the other
• Clean simple looking card
Nice to have
• Round corners and detail like raised or spot UV
• Something that stands out
Should not have
• To title needed, Director etc

```html
<!DOCTYPE html>
<html lang="en">
<head>
<meta charset="utf-8">
<title>Stone Range – Business Cards</title>
<link rel="stylesheet" href="https://fonts.googleapis.com/css2?family=Oswald:wght@500&family=Poppins:wght@300;400;500&display=swap">
<style>
  :root {
    --backdrop: #2e2925;
    --card: #202021;
    --edge: #e01818;
    --gloss: #141414;
    --gloss-soft: #303031;
    --ink-white: #f2f2f2;
    --ink-grey: #d6d6d6;
  }
  html, body {
    margin: 0;
    padding: 0;
    width: 1200px;
    height: 1055px;
    overflow: hidden;
    background: var(--backdrop);
  }
  .sheet {
    width: 1200px;
    height: 1055px;
    display: flex;
    flex-direction: column;
    align-items: center;
    justify-content: center;
    gap: 60px;
  }
  .card {
    position: relative;
    width: 760px;
    height: 434px;
    background: var(--card);
    border-radius: 34px;
    box-shadow: 0 0 0 3px var(--edge), 0 18px 40px rgba(0,0,0,0.45);
    box-sizing: border-box;
  }
  /* Front: logo side */
  .card--front {
    display: flex;
    align-items: center;
    justify-content: center;
  }
  .brand {
    display: flex;
    flex-direction: column;
    align-items: flex-start;
  }
  .brand__row {
    display: flex;
    align-items: center;
    gap: 18px;
  }
  .brand__mark {
    width: 52px;
    height: 52px;
    background: var(--gloss);
    box-shadow: inset 0 1px 0 var(--gloss-soft);
  }
  .brand__name {
    font-family: 'Poppins', sans-serif;
    font-weight: 500;
    font-size: 74px;
    line-height: 1;
    color: var(--gloss);
    letter-spacing: 0.5px;
  }
  .brand__tagline {
    margin-top: 14px;
    margin-left: 70px;
    font-family: 'Poppins', sans-serif;
    font-weight: 400;
    font-size: 21px;
    letter-spacing: 1px;
    color: var(--gloss);
  }
  /* Back: details side */
  .card--back {
    display: flex;
    align-items: center;
    justify-content: center;
    gap: 34px;
  }
  .holder {
    margin: 0;
    font-family: 'Oswald', sans-serif;
    font-weight: 500;
    font-size: 34px;
    letter-spacing: 0.5px;
    text-transform: uppercase;
    color: var(--ink-white);
  }
  .divider {
    width: 2px;
    height: 92px;
    background: var(--ink-grey);
  }
  .contact {
    list-style: none;
    margin: 0;
    padding: 0;
    font-family: 'Poppins', sans-serif;
    font-weight: 300;
    font-size: 19px;
    color: var(--ink-grey);
  }
  .contact__item {
    display: flex;
    align-items: center;
    gap: 12px;
    line-height: 30px;
  }
  .contact__icon {
    width: 15px;
    height: 15px;
    flex: none;
    fill: var(--ink-grey);
  }
  .contact__icon--line {
    fill: none;
    stroke: var(--ink-grey);
    stroke-width: 1.4;
  }
</style>
</head>
<body>
<main class="sheet">
  <section class="card card--front" aria-label="Card front">
    <div class="brand">
      <div class="brand__row">
        <span class="brand__name">Stone Range</span>
        <span class="brand__mark" aria-hidden="true"></span>
      </div>
      <span class="brand__tagline">Houses shaped for life.</span>
    </div>
  </section>

  <section class="card card--back" aria-label="Card back">
    <h1 class="holder">Derek Haskins</h1>
    <span class="divider" aria-hidden="true"></span>
    <ul class="contact">
      <li class="contact__item">
        <svg class="contact__icon" viewBox="0 0 16 16" aria-hidden="true"><path d="M3.2 1 5.6 3.6 4.5 5.6c.9 2.2 3.6 4.9 5.9 5.9l2-1.1L15 12.8l-1.6 2.1C7.6 15 1 8.4 1.1 2.6z"/></svg>
        <span>0274930268</span>
      </li>
      <li class="contact__item">
        <svg class="contact__icon contact__icon--line" viewBox="0 0 16 16" aria-hidden="true"><rect x="1.5" y="3.5" width="13" height="9"/><path d="M1.5 3.5 8 8.5l6.5-5"/></svg>
        <span>derekh@stonerange.co.nz</span>
      </li>
      <li class="contact__item">
        <svg class="contact__icon contact__icon--line" viewBox="0 0 16 16" aria-hidden="true"><circle cx="8" cy="8" r="6.5"/><ellipse cx="8" cy="8" rx="2.8" ry="6.5"/><path d="M1.5 8h13"/></svg>
        <span>www.stonerange.co.nz</span>
      </li>
    </ul>
  </section>
</main>
</body>
</html>
```